Conservative, Modern and Sharp Builder Business card

Hi there,
We would like to update our existing business card.
I have attached photos of existing business card, logo and van sign.

I would like the business card to also list what we do :
Renovation • New Build • Alteration
Extension • Bathroom • Maintenance.(Seperated by dots)

Contact number : 021 0483 0752
(With that exact spacing)

Ideally when people looking from about 2-3 metres, they know that it is a builder’s business card

Open to suggestions on fonts, layout, style of business card

PLEASE ONLY SUBMIT YOUR BEST OR MAX 3 DESIGNS FOR EACH DESIGNER

Thanks

Construction. Renovation

Details should be the same as the existing card. And addition of what we do.

• The new business card must not have the same layout as our existing one. Thanks

```html
<!DOCTYPE html>
<html lang="en">
<head>
<meta charset="utf-8">
<title>KeelBuild Business Card</title>
<link href="https://fonts.googleapis.com/css2?family=Poppins:wght@400;500;700;800&display=swap" rel="stylesheet">
<style>
  :root {
    --bg: #2e2e2e;
    --ink: #111111;
    --paper: #ffffff;
    --muted: #9a9a9a;
    --rule: #cfcfcf;
  }
  * { box-sizing: border-box; margin: 0; padding: 0; }
  html, body { width: 1200px; height: 689px; overflow: hidden; }
  body {
    background: var(--bg);
    font-family: "Poppins", sans-serif;
    position: relative;
  }
  .card {
    position: absolute;
    top: 194px;
    width: 525px;
    height: 300px;
    border-radius: 18px;
    overflow: hidden;
  }
  /* Front */
  .card-front { left: 45px; background: var(--ink); color: var(--paper); }
  .brand {
    position: absolute; left: 0; right: 0; top: 58px;
    display: flex; align-items: center; justify-content: center; gap: 12px;
  }
  .brand-square { width: 16px; height: 16px; background: currentColor; }
  .brand-name { font-weight: 800; font-size: 46px; letter-spacing: 0.5px; line-height: 1; }
  .front-rule {
    position: absolute; left: 70px; right: 70px; height: 1px; background: var(--muted);
  }
  .front-rule.top { top: 135px; }
  .front-rule.bottom { top: 262px; }
  .services {
    position: absolute; left: 70px; right: 70px; top: 152px;
    display: grid; grid-template-columns: repeat(3, 1fr); row-gap: 4px;
    list-style: none; font-size: 15px; font-weight: 400;
  }
  .services li::before { content: "\2022"; margin-right: 8px; }
  .services li:nth-child(3n+2) { padding-left: 18px; }
  .services li:nth-child(3n) { padding-left: 36px; }
  .contact-line {
    position: absolute; left: 0; right: 0; top: 222px; text-align: center;
    font-size: 16px; letter-spacing: 0.3px;
  }
  .contact-line strong { font-weight: 700; font-size: 18px; }

  /* Back */
  .card-back { left: 630px; background: var(--paper); color: var(--ink); }
  .card-back .brand { left: 0; right: auto; width: 250px; top: 108px; }
  .card-back .brand-name { font-size: 38px; }
  .divider {
    position: absolute; left: 262px; top: 40px; width: 1px; height: 150px;
    background: linear-gradient(var(--paper), var(--muted), var(--paper));
  }
  .person { position: absolute; left: 285px; top: 38px; }
  .person-name { font-weight: 700; font-size: 21px; line-height: 1.1; }
  .person-role { font-size: 13px; color: #444; margin-bottom: 14px; }
  .contacts { list-style: none; font-size: 13px; line-height: 1.65; }
  .contacts li { display: flex; align-items: center; gap: 8px; }
  .contacts svg { width: 13px; height: 13px; flex: none; }
  .band-line {
    position: absolute; left: 0; right: 0; top: 246px; height: 5px; background: var(--ink);
  }
  .band-base {
    position: absolute; left: 0; right: 0; bottom: 0; height: 30px; background: var(--ink);
  }
  .band-base::before {
    content: ""; position: absolute; left: 0; right: 0; top: 7px; height: 3px; background: var(--paper);
  }
  .corner-block {
    position: absolute; right: 0; top: 196px; width: 118px; height: 50px; background: var(--ink);
    clip-path: polygon(22% 0, 100% 0, 100% 100%, 0 100%);
  }
  .corner-square {
    position: absolute; right: 34px; top: 210px; width: 22px; height: 22px; background: var(--paper);
  }
  .corner-rule {
    position: absolute; right: 0; top: 190px; width: 130px; height: 3px; background: var(--ink);
  }
</style>
</head>
<body>
  <section class="card card-front">
    <div class="brand"><span class="brand-square"></span><span class="brand-name">KeelBuild</span></div>
    <div class="front-rule top"></div>
    <ul class="services">
      <li>Renovation</li><li>Alteration</li><li>Bathroom</li>
      <li>New Build</li><li>Extension</li><li>Maintenance</li>
    </ul>
    <p class="contact-line">Contact number : <strong>021 0483 0752</strong></p>
    <div class="front-rule bottom"></div>
  </section>

  <section class="card card-back">
    <div class="brand"><span class="brand-square"></span><span class="brand-name">KeelBuild</span></div>
    <div class="divider"></div>
    <div class="person">
      <p class="person-name">Tomas Varga</p>
      <p class="person-role">Residential Builder</p>
      <ul class="contacts">
        <li><svg viewBox="0 0 24 24"><path fill="currentColor" d="M6.6 10.8a15 15 0 006.6 6.6l2.2-2.2a1 1 0 011-.25 11.4 11.4 0 003.6.57 1 1 0 011 1V20a1 1 0 01-1 1A17 17 0 013 4a1 1 0 011-1h3.5a1 1 0 011 1c0 1.25.2 2.45.57 3.6a1 1 0 01-.25 1z"/></svg>021-0483-0752</li>
        <li><svg viewBox="0 0 24 24"><path fill="currentColor" d="M2 5h20v14H2z"/><path fill="none" stroke="#fff" stroke-width="1.8" d="M2 5l10 8 10-8"/></svg>KeelBuild@mail.nz</li>
        <li><svg viewBox="0 0 24 24" fill="none" stroke="currentColor" stroke-width="1.8"><circle cx="12" cy="12" r="9.5"/><path d="M2.5 12h19M12 2.5c3 3 3 16 0 19M12 2.5c-3 3-3 16 0 19"/></svg>www.KeelBuild.nz</li>
        <li><svg viewBox="0 0 24 24"><circle cx="12" cy="12" r="9" fill="none" stroke="currentColor" stroke-width="2"/></svg>KeelBuild.nz</li>
      </ul>
    </div>
    <div class="corner-rule"></div>
    <div class="corner-block"></div>
    <div class="corner-square"></div>
    <div class="band-line"></div>
    <div class="band-base"></div>
  </section>
</body>
</html>
```